Media Training Presentation (template)

This is a 49-slide power point deck to be used in training clients to deal with the media in various settings. We need a template we can personalize for different clients. The overall color scheme should match our logo. It should look very professional, but also engaging. The word doc contains all of the text, images, and videos for each slide. Also uploaded our logo. Please match/coordinate colors of presentation to the logo colors. If you prefer, you can submit five or six slides showing the overall design and a template for each type of slide, then complete the remainder of the slides within 24 hours if chosen. (Sorry for the quick turnaround…we didn’t know we would need it this quickly!) Thanks for submitting!
Target Market(s)
Government and corporate clients
Look and feel

```html
<!DOCTYPE html>
<html lang="en">
<head>
<meta charset="utf-8">
<title>HC Media Training – Slide Templates</title>
<link href="https://fonts.googleapis.com/css2?family=Karla:wght@400;500;700;800&family=Work+Sans:wght@300;400;500&display=swap" rel="stylesheet">
<style>
  :root{
    --brand-blue:#0a56c2;
    --brand-blue-deep:#0b3f9a;
    --brand-navy:#0e2f7a;
    --ink:#4a4a4a;
    --paper:#ffffff;
    --canvas:#ffffff;
    --icon-grey:#8a8a8a;
    --icon-sky:#3aa0f0;
    --icon-dark:#2c2c2c;
  }
  *{box-sizing:border-box;margin:0;padding:0}
  html,body{width:1200px;height:2194px;overflow:hidden;background:var(--canvas)}
  body{position:relative;font-family:"Karla",sans-serif;color:var(--ink)}

  .slide{position:absolute;width:552px;height:310px;background:var(--paper);overflow:hidden;
    box-shadow:14px 16px 28px rgba(0,0,0,.28)}
  .slide--cover{left:124px;top:87px}
  .slide--agenda{left:520px;top:423px}
  .slide--section{left:124px;top:760px}
  .slide--pillars{left:520px;top:1096px}
  .slide--quote{left:124px;top:1432px}
  .slide--goals{left:520px;top:1769px}

  .photo{position:absolute}

  .brand{position:absolute;top:24px;right:18px;display:flex;align-items:center;gap:4px;
    font-family:"Work Sans",sans-serif;font-weight:400;font-size:8px;letter-spacing:.4px;color:var(--brand-blue)}
  .brand__mark{width:9px;height:9px;background:var(--brand-blue)}

  .corner-brand{position:absolute;right:18px;bottom:7px;display:flex;align-items:center;gap:4px;
    font-family:"Work Sans",sans-serif;font-size:7px;letter-spacing:.4px;color:var(--brand-blue)}
  .corner-brand__mark{width:14px;height:14px;border:2px solid var(--brand-blue)}

  .footer{position:absolute;left:23px;bottom:8px;font-size:5px;color:#333}

  .kicker{position:absolute;left:34px;top:9px;font-size:8px;color:#444}
  .heading{position:absolute;left:34px;top:22px;font-family:"Karla",sans-serif;font-weight:700;font-size:18px;color:var(--ink)}

  /* cover */
  .cover__photo{inset:0;background:
    radial-gradient(ellipse 90px 70px at 78% 22%,#e2542e 0%,rgba(226,84,46,.55) 45%,rgba(226,84,46,0) 100%),
    radial-gradient(ellipse 110px 110px at 80% 72%,#1c1b1d 0%,rgba(28,27,29,.85) 55%,rgba(28,27,29,0) 100%),
    radial-gradient(ellipse 160px 140px at 30% 45%,#efe8de 0%,rgba(239,232,222,0) 100%),
    linear-gradient(100deg,#d9cdbd 0%,#cdb894 40%,#a88d68 60%,#5c5048 78%,#2b2a2c 100%)}
  .cover__panel{position:absolute;left:24px;top:31px;width:285px;height:249px;border-radius:0 0 40px 0;
    background:rgba(255,255,255,.72)}
  .cover__brand{position:absolute;left:48px;top:84px;font-family:"Work Sans",sans-serif;color:var(--brand-blue)}
  .cover__brand-name{font-size:24px;font-weight:400;letter-spacing:1px;line-height:1}
  .cover__brand-sub{font-size:10px;letter-spacing:3.4px;color:#4a6aa8;margin-top:1px}
  .cover__title{position:absolute;left:48px;top:148px;font-family:"Work Sans",sans-serif;font-weight:400;font-size:26px;color:var(--brand-blue)}
  .cover__subtitle{position:absolute;left:48px;top:186px;font-family:"Work Sans",sans-serif;font-size:15px;color:var(--brand-blue)}
  .cover__name{position:absolute;left:48px;top:210px;font-family:"Work Sans",sans-serif;font-size:14px;color:var(--brand-blue)}
  .cover__role{position:absolute;left:48px;top:230px;font-size:7px;color:var(--brand-blue)}
  .cover__date{position:absolute;left:48px;top:247px;font-family:"Work Sans",sans-serif;font-size:11px;color:var(--brand-blue)}
  .cover__footer{position:absolute;left:118px;bottom:8px;font-family:"Work Sans",sans-serif;font-size:8px;letter-spacing:3px;color:#fff}

  /* agenda */
  .agenda__band{position:absolute;left:0;top:47px;width:552px;height:236px;background:#1c1a2a}
  .agenda__panel{position:absolute;left:10px;top:47px;width:224px;height:236px;
    background:linear-gradient(90deg,var(--brand-blue-deep),#1148a8)}
  .agenda__photo{left:234px;top:47px;width:318px;height:236px;background:
    radial-gradient(ellipse 70px 45px at 62% 45%,#7d8fa8 0%,rgba(125,143,168,.5) 50%,rgba(125,143,168,0) 100%),
    radial-gradient(ellipse 120px 90px at 85% 20%,#b04ab8 0%,rgba(176,74,184,0) 100%),
    radial-gradient(ellipse 110px 80px at 20% 15%,#6a3a5a 0%,rgba(106,58,90,0) 100%),
    radial-gradient(ellipse 90px 70px at 15% 85%,#3a2040 0%,rgba(58,32,64,0) 100%),
    linear-gradient(90deg,#2a1d2e 0%,#3a2442 50%,#4a2a55 100%)}
  .agenda__title{position:absolute;left:38px;top:12px;color:#fff;font-size:10px}
  .agenda__list{position:absolute;left:34px;top:35px;list-style:none}
  .agenda__item{display:flex;align-items:center;height:22px;color:#fff}
  .agenda__num{width:21px;font-size:9.5px}
  .agenda__text{border-left:1px solid rgba(255,255,255,.6);padding-left:6px;font-size:7.5px;line-height:16px}

  /* section */
  .section__photo{left:29px;top:53px;width:290px;height:219px;background:
    radial-gradient(ellipse 80px 60px at 50% 35%,#2a2a2c 0%,rgba(42,42,44,.7) 55%,rgba(42,42,44,0) 100%),
    radial-gradient(ellipse 110px 120px at 45% 75%,#c0282c 0%,rgba(192,40,44,.6) 55%,rgba(192,40,44,0) 100%),
    radial-gradient(ellipse 60px 80px at 8% 20%,#b8c83a 0%,rgba(184,200,58,0) 100%),
    linear-gradient(90deg,#4a4a3e 0%,#8a3a34 40%,#a83030 60%,#6a6c6a 85%,#8a9aa8 100%)}
  .section__panel{position:absolute;left:304px;top:53px;width:227px;height:219px;border-radius:26px 0 30px 0;
    background:
    radial-gradient(ellipse 80px 60px at 70% 25%,#6a9ae0 0%,rgba(106,154,224,0) 100%),
    radial-gradient(ellipse 90px 60px at 30% 85%,#5a8ad8 0%,rgba(90,138,216,0) 100%),
    linear-gradient(160deg,#2a6ad0,#0f49b0 60%,#1c5cc4)}
  .section__title{position:absolute;left:320px;top:111px;font-weight:800;font-size:30px;line-height:1.12;color:#fff;
    text-shadow:0 1px 3px rgba(0,0,0,.35)}

  /* pillars */
  .pillars__band{position:absolute;left:0;top:150px;width:552px;height:160px;background:var(--brand-blue)}
  .pillar{position:absolute;top:85px;width:134px;text-align:center}
  .pillar__photo{position:relative;width:134px;height:113px;border-radius:6px 0 14px 0;box-shadow:0 2px 6px rgba(0,0,0,.25)}
  .pillar__caption{margin-top:16px;font-size:11.5px;line-height:1.2;color:#fff}
  .pillar--one{left:53px}
  .pillar--two{left:211px}
  .pillar--three{left:368px}
  .pillar--one .pillar__photo{background:
    radial-gradient(ellipse 35px 30px at 18% 85%,#f0c81a 0%,rgba(240,200,26,0) 100%),
    radial-gradient(ellipse 28px 40px at 20% 45%,#4a3024 0%,rgba(74,48,36,0) 100%),
    radial-gradient(ellipse 22px 30px at 72% 35%,#2a2a2a 0%,rgba(42,42,42,0) 100%),
    linear-gradient(90deg,#d8d2c8 0%,#e8eef4 50%,#c8d4e2 100%)}
  .pillar--two .pillar__photo{background:
    radial-gradient(ellipse 30px 25px at 50% 55%,#1e1e1e 0%,rgba(30,30,30,0) 100%),
    radial-gradient(ellipse 40px 35px at 25% 25%,#9a8a7a 0%,rgba(154,138,122,0) 100%),
    radial-gradient(ellipse 40px 30px at 80% 30%,#b0b4b8 0%,rgba(176,180,184,0) 100%),
    linear-gradient(160deg,#6a6a6a,#3e3e40 50%,#8a8a8c)}
  .pillar--three .pillar__photo{background:
    radial-gradient(ellipse 45px 25px at 60% 28%,#f4f0e0 0%,rgba(244,240,224,0) 100%),
    radial-gradient(ellipse 30px 30px at 80% 80%,#4a4038 0%,rgba(74,64,56,0) 100%),
    radial-gradient(ellipse 28px 28px at 35% 82%,#2e2a28 0%,rgba(46,42,40,0) 100%),
    linear-gradient(180deg,#e6e8ea 0%,#c8c0b0 55%,#8a7e70 100%)}
  .pillars__page{position:absolute;right:26px;bottom:9px;font-size:5px;color:#fff}
  .slide--pillars .footer{color:#fff}

  /* quote */
  .quote__panel{position:absolute;left:21px;top:58px;width:200px;height:210px;border-radius:30px 0 0 0;background:var(--brand-blue)}
  .quote__photo{left:212px;top:58px;width:319px;height:210px;border-radius:26px 0 30px 0;background:
    radial-gradient(ellipse 70px 85px at 48% 45%,#c89078 0%,rgba(200,144,120,.6) 50%,rgba(200,144,120,0) 100%),
    radial-gradient(ellipse 90px 40px at 45% 95%,#2e2e34 0%,rgba(46,46,52,0) 100%),
    radial-gradient(ellipse 60px 70px at 85% 55%,#5a5448 0%,rgba(90,84,72,0) 100%),
    linear-gradient(110deg,#8a9a86 0%,#9aa08c 35%,#7a7866 70%,#5a584c 100%)}
  .quote__text{position:absolute;left:38px;top:112px;width:170px;font-weight:800;font-size:17px;line-height:1.17;color:#fff}

  /* goals */
  .goals__photo{left:29px;top:66px;width:249px;height:206px;border-radius:14px 0 24px 0;background:
    radial-gradient(circle at 37% 54%,#3a3634 0,#5a524c 18%,#2a2828 26%,rgba(233,233,233,0) 27.5%),
    radial-gradient(ellipse 50px 60px at 85% 30%,#cfcfcf 0%,rgba(207,207,207,0) 100%),
    radial-gradient(ellipse 50px 50px at 60% 15%,#d6d6d6 0%,rgba(214,214,214,0) 100%),
    linear-gradient(180deg,#ececec,#f4f4f4)}
  .goals__list{position:absolute;left:308px;top:71px;list-style:none}
  .goal{display:flex;align-items:center;height:38px;margin-bottom:17px}
  .goal__icon{width:38px;height:38px;display:flex;align-items:center;justify-content:center}
  .goal__icon--navy{background:var(--brand-navy)}
  .goal__icon--grey{background:var(--icon-grey)}
  .goal__icon--sky{background:var(--icon-sky)}
  .goal__icon--dark{background:var(--icon-dark)}
  .goal__label{margin-left:10px;font-weight:700;font-size:11.5px;color:#555}
</style>
</head>
<body>

<section class="slide slide--cover">
  <div class="photo cover__photo" role="img" aria-label="Blurred office scene behind a camera rig with an orange-framed field monitor"></div>
  <svg width="552" height="310" style="position:absolute;left:0;top:0" aria-hidden="true">
    <path d="M335 10 H60 Q12 10 12 58 V310" fill="none" stroke="#0a56c2" stroke-width="24"/>
    <path d="M323 180 V240 Q323 292 270 292" fill="none" stroke="#0a56c2" stroke-width="24"/>
  </svg>
  <div class="cover__panel"></div>
  <div class="cover__brand">
    <div class="cover__brand-name">HARWELL</div>
    <div class="cover__brand-sub">COMMUNICATIONS</div>
  </div>
  <h1 class="cover__title">HC Media Training</h1>
  <p class="cover__subtitle">Your subtitle slide goes here</p>
  <p class="cover__name">Dana Whitcombe</p>
  <p class="cover__role">CEO &amp; Founder</p>
  <p class="cover__date">July 2023</p>
  <p class="cover__footer">Harwell Communications - HC Media Training</p>
</section>

<section class="slide slide--agenda">
  <div class="brand"><span class="brand__mark"></span>HARWELL</div>
  <div class="agenda__band"></div>
  <div class="photo agenda__photo" role="img" aria-label="Camera on a tripod filming an interview in a purple-lit studio"></div>
  <div class="agenda__panel">
    <p class="agenda__title">Agenda</p>
    <ol class="agenda__list">
      <li class="agenda__item"><span class="agenda__num">01</span><span class="agenda__text">Introduction to Media Training</span></li>
      <li class="agenda__item"><span class="agenda__num">02</span><span class="agenda__text">Lorem Ipsum simply dummy text</span></li>
      <li class="agenda__item"><span class="agenda__num">03</span><span class="agenda__text">Lorem Ipsum simply dummy text</span></li>
      <li class="agenda__item"><span class="agenda__num">04</span><span class="agenda__text">Lorem Ipsum simply dummy text</span></li>
      <li class="agenda__item"><span class="agenda__num">05</span><span class="agenda__text">Lorem Ipsum simply dummy text</span></li>
      <li class="agenda__item"><span class="agenda__num">06</span><span class="agenda__text">Lorem Ipsum simply dummy text</span></li>
      <li class="agenda__item"><span class="agenda__num">07</span><span class="agenda__text">Lorem Ipsum simply dummy text</span></li>
      <li class="agenda__item"><span class="agenda__num">08</span><span class="agenda__text">Lorem Ipsum simply dummy text</span></li>
      <li class="agenda__item"><span class="agenda__num">09</span><span class="agenda__text">Lorem Ipsum simply dummy text</span></li>
    </ol>
  </div>
  <p class="footer">Harwell Communications &nbsp;- HC Media Training</p>
  <div class="corner-brand"><span class="corner-brand__mark"></span>HARWELL</div>
</section>

<section class="slide slide--section">
  <div class="brand"><span class="brand__mark"></span>HARWELL</div>
  <div class="photo section__photo" role="img" aria-label="Camera operator in a red shirt filming at an outdoor event"></div>
  <div class="section__panel" role="img" aria-label="Blue-tinted crowd of press photographers"></div>
  <h2 class="section__title">Introduction<br>to Media<br>Training</h2>
  <p class="footer">Harwell Communications &nbsp;- HC Media Training</p>
  <div class="corner-brand"><span class="corner-brand__mark"></span>HARWELL</div>
</section>

<section class="slide slide--pillars">
  <p class="kicker">Introduction to Media Training</p>
  <h2 class="heading">What is media training?</h2>
  <div class="brand"><span class="brand__mark"></span>HARWELL</div>
  <div class="pillars__band"></div>
  <div class="pillar pillar--one">
    <div class="pillar__photo" role="img" aria-label="Woman filming herself with a phone on a gimbal"></div>
    <p class="pillar__caption">It’s not natural.</p>
  </div>
  <div class="pillar pillar--two">
    <div class="pillar__photo" role="img" aria-label="Camera on a tripod recording a rehearsal"></div>
    <p class="pillar__caption">It requires practice.</p>
  </div>
  <div class="pillar pillar--three">
    <div class="pillar__photo" role="img" aria-label="Team in a planning workshop around a whiteboard"></div>
    <p class="pillar__caption">It’s about developing a mindset.</p>
  </div>
  <p class="footer">Harwell Communications &nbsp;- HC Media Training</p>
  <p class="pillars__page">4</p>
</section>

<section class="slide slide--quote">
  <p class="kicker">Introduction to Media Training</p>
  <div class="brand"><span class="brand__mark"></span>HARWELL</div>
  <div class="quote__panel"></div>
  <div class="photo quote__photo" role="img" aria-label="Still from a televised interview with a public figure"></div>
  <p class="quote__text">Training and<br>preparation are<br>the difference<br>between success<br>and failure.</p>
  <p class="footer">Harwell Communications &nbsp;- HC Media Training</p>
  <div class="corner-brand"><span class="corner-brand__mark"></span>HARWELL</div>
</section>

<section class="slide slide--goals">
  <p class="kicker">Introduction to Media Training</p>
  <h2 class="heading">Goals:</h2>
  <div class="brand"><span class="brand__mark"></span>HARWELL</div>
  <div class="photo goals__photo" role="img" aria-label="Faded meeting-room scene with a circular cut-out of colleagues reviewing documents"></div>
  <ul class="goals__list">
    <li class="goal">
      <span class="goal__icon goal__icon--navy">
        <svg width="22" height="22" viewBox="0 0 22 22" fill="none" stroke="#fff" stroke-width="1.4"><rect x="7" y="2" width="13" height="9"/><circle cx="4" cy="8" r="2"/><path d="M4 10v6M2 13h4"/><path d="M2 20h18M6 20v-2M11 20v-2M16 20v-2"/></svg>
      </span>
      <span class="goal__label">Learn how to prepare</span>
    </li>
    <li class="goal">
      <span class="goal__icon goal__icon--grey">
        <svg width="22" height="22" viewBox="0 0 22 22" fill="#fff"><rect x="3" y="14" width="7" height="5"/><circle cx="6.5" cy="8" r="3.5"/><rect x="12" y="14" width="7" height="5"/><rect x="13" y="5" width="5" height="9"/><rect x="12" y="3" width="7" height="2"/></svg>
      </span>
      <span class="goal__label">Develop a strategy</span>
    </li>
    <li class="goal">
      <span class="goal__icon goal__icon--sky">
        <svg width="22" height="22" viewBox="0 0 22 22" fill="none" stroke="#fff" stroke-width="1.6"><circle cx="11" cy="11" r="4" fill="#fff"/><path d="M11 1v4M11 17v4M1 11h4M17 11h4M4 4l3 3M15 15l3 3M18 4l-3 3M4 18l3-3"/></svg>
      </span>
      <span class="goal__label">Clarify message</span>
    </li>
    <li class="goal">
      <span class="goal__icon goal__icon--dark">
        <svg width="22" height="22" viewBox="0 0 22 22" fill="none" stroke="#fff" stroke-width="1.2"><rect x="2" y="8" width="18" height="12"/><path d="M2 12h18M2 16h18M8 8v4M14 8v4M5 12v4M11 12v4M17 12v4M8 16v4M14 16v4"/><path d="M14 6l5-4"/></svg>
      </span>
      <span class="goal__label">Build a practice approach</span>
    </li>
  </ul>
  <p class="footer">Harwell Communications &nbsp;- HC Media Training</p>
  <div class="corner-brand"><span class="corner-brand__mark"></span>HARWELL</div>
</section>

</body>
</html>
```